Web design for Crowdfunding site HarborWings.net

We need a web design for christian crowdfunding website. Here is the challenge: We need responsive layout that is targeted first in iPad size of screen. It should also scale somehow down to iPhone size of screens. Web layout can be about the same size as iPad screen.

Screens should work so that main page scrolls not but only certain part of the screen scrolls and always one "page" at time. We can implement these "scrolls" then later with javascript but now we need only design. The challenge is to create this kind of hybrid website / app look.

Target is at first to raise funds to orphan people needing about $40 per month for their living and education. There is always some organization which takes care of these kids. Later there will be other christian missions included. At first we are looking to find monthly supporters.

You can be as creative as you want :) As you see from the look and feel sector, I am not looking any same traditional look which many "help kids" sites have. I am looking to reach now younger generation and therefore iPad and mobile are the main screen sizes.

Inspirational designs:
- https://pixelfair.example/profiles/studiolumkin/designs/482613?from=%2Fbrowse%2Fxhr%2Fworks%3Fcategory%3Dmobile-app-design
- http://www.artboardhub.example/design/7264158 Clear, simple visuals
- http://www.artboardhub.example/design/8391027 Header
- http://www.artboardhub.example/design/6470952 Contrast in the colors, i think is powerfull

Some terms could be: Kids play, kids are learning (in the school). No static posture but living like kids are. I wonder also how we could also add little bit gaming style even though the question is of reali life of real people. Giving should be rewarding.

Target Market(s)

People who want help other people.

Industry/Entity Type

Christian

Number of Pages Required

4 page

Requirements
Must have
• Homepage. Mission page (In my wireframes it was one kid).
Nice to have
• Other pages and some idea how to scroll. 4 pages is no must. If you feel easy, please give first some draft and I give comments on that.

```html
<!DOCTYPE html>
<html lang="en">
<head>
<meta charset="utf-8">
<title>HarborWings – Mission Page</title>
<link rel="stylesheet" href="https://fonts.googleapis.com/css2?family=Lato:wght@700;900&family=Roboto:wght@400;500;700&family=Tinos:wght@700&display=swap">
<style>
:root{
  --green:#2fcb6f;
  --teal:#27a394;
  --teal-square:#2aa79a;
  --ink:#222327;
  --muted:#6d6e75;
  --about-bg:#d6d5e3;
  --activities-bg:#e8e7ef;
  --team-bg:#cfcedd;
  --card:#ffffff;
  --tab-bg:#c9c9cd;
  --tab-active:#ececee;
  --orange:#f07c22;
  --blue:#2f7de1;
  --red:#e8262d;
  --footer:#3c3c3e;
  --placeholder:#fbfbf3;
  --avatar:#d9d9de;
  --silhouette:#8f8f96;
}
*{box-sizing:border-box;margin:0;padding:0}
html,body{width:1200px;height:3000px;overflow:hidden;background:#fff}
body{font-family:"Roboto",Arial,sans-serif;color:var(--ink)}
.canvas{position:relative;width:1200px;height:3000px;overflow:hidden}
.abs{position:absolute}

/* Header */
.site-header{position:absolute;left:0;top:0;width:1200px;height:66px;background:var(--green);color:#fff}
.menu-toggle{position:absolute;left:20px;top:20px;width:40px;height:28px}
.menu-toggle span{display:block;height:5px;background:#fff;margin-bottom:6px;border-radius:1px}
.nav-missions{position:absolute;left:73px;top:23px;font:700 16px "Lato",sans-serif}
.brand{position:absolute;left:0;width:1200px;top:4px;text-align:center;font:900 46px/58px "Lato",sans-serif;letter-spacing:2px}
.auth{position:absolute;right:22px;top:23px;font:700 17px "Lato",sans-serif}
.auth span{margin-left:20px}

/* Hero */
.hero{position:absolute;left:0;top:66px;width:1200px;height:750px;
  background:
   radial-gradient(ellipse 300px 360px at 330px 460px,rgba(70,66,60,.55),rgba(70,66,60,0) 70%),
   radial-gradient(ellipse 380px 420px at 820px 400px,rgba(60,56,50,.6),rgba(60,56,50,0) 72%),
   radial-gradient(ellipse 180px 160px at 830px 330px,rgba(235,230,222,.55),rgba(235,230,222,0) 75%),
   radial-gradient(ellipse 140px 130px at 320px 400px,rgba(230,225,216,.5),rgba(230,225,216,0) 75%),
   linear-gradient(180deg,#f3f1ed 0%,#e2ded7 30%,#b9b4ac 70%,#8e8982 100%)}
.hero-quote{position:absolute;left:0;top:10px;width:1076px;text-align:center}
.hero-quote .verse{color:var(--green);font-size:14px;line-height:19px;font-weight:500}
.hero-quote .pledge{color:#111;font-size:17px;font-weight:700;margin-top:2px}
.hero-quote .pledge b{color:var(--red)}
.hero-band{position:absolute;left:0;top:816px;width:1200px;height:36px;background:var(--green)}

/* Sections */
.section{position:absolute;left:0;width:1200px;overflow:hidden}
.section-about{top:852px;height:680px;background:var(--about-bg)}
.section-activities{top:1532px;height:704px;background:var(--activities-bg)}
.section-team{top:2236px;height:674px;background:var(--team-bg)}
.section-title{position:absolute;left:0;width:1200px;text-align:center;font:700 46px/52px "Tinos",serif;color:#111;letter-spacing:1px}

.mission-title{font-size:26px;color:#2a2a2a;white-space:nowrap}
.tabs{display:flex;height:26px;background:var(--tab-bg)}
.tabs div{flex:1;text-align:center;font-size:11px;line-height:26px;color:#333}
.tabs .active{background:var(--tab-active)}
.story p{font-size:13.5px;line-height:15.5px;color:#1f1f1f;margin-bottom:15px}
.img-placeholder{background:var(--placeholder);border:2px solid #444}

.timeline-rail{position:absolute;width:7px;background:#a6a6ad;border-radius:3px}
.timeline-dot{position:absolute;width:30px;height:30px;border-radius:50%;background:#9d9da3}
.timeline-dot.current{background:var(--orange)}

/* Support panel */
.kid-name{font-size:26px;color:#2a2a2a;white-space:nowrap}
.meta{font-size:14px;color:#333;display:flex;align-items:center;gap:10px}
.support-row{display:flex;align-items:center;font-size:13px;color:#333;border-bottom:1px solid #9a9aa3;padding-bottom:8px}
.support-row .angels{display:flex;gap:8px;margin-left:auto;align-items:center}
.angel{width:22px;height:22px;border-radius:50%;background:#bdbdc4;border:2px solid #8c8c93;overflow:hidden;display:block}
.angel svg{display:block;width:100%;height:100%}
.my-support{font-size:13px;font-weight:700;color:#222;display:flex;align-items:center;gap:14px;white-space:nowrap}
.close-dot{width:20px;height:20px;border-radius:50%;background:#fff;color:#aaa;font-size:13px;line-height:20px;text-align:center}
.progress{display:flex;gap:14px;align-items:flex-start}
.progress-box{width:128px;height:108px;background:#c3c3cb;display:flex;align-items:center;justify-content:center}
.progress-text{padding-top:20px;font-size:12px;color:#333;line-height:26px;white-space:nowrap}
.progress-text strong{font-size:15px}
.participate-label{font-size:14px;color:#333;border-bottom:1px solid #9a9aa3;padding-bottom:8px}
.option{position:absolute;height:40px;background:var(--card);display:flex;align-items:center;padding-left:12px;font-size:14px;font-weight:500;color:#222;white-space:nowrap;box-shadow:0 1px 1px rgba(0,0,0,.12)}
.option .check{width:24px;height:24px;background:var(--teal-square);margin-right:16px;border-radius:2px;flex:none}
.option .cart{margin-left:auto;margin-right:14px;flex:none}
.amount-input{width:110px;height:30px;border:1px dashed #bbb;font-size:12px;line-height:28px;padding-left:10px;margin-left:14px;color:#333;background:#fff;flex:none}

/* Activities */
.profile-avatar{position:absolute;width:142px;height:142px;border-radius:50%;background:var(--avatar);border:5px solid #9e9ea5;overflow:hidden}
.profile-avatar svg,.mission-card .avatar svg,.follow-item i svg{display:block;width:100%;height:100%}
.profile-field{font-size:15px;color:#222}
.label-caps{font-size:14px;color:#333;letter-spacing:.3px}
.follow-item{display:flex;align-items:center;gap:12px;font-size:14px;color:#333;height:34px}
.follow-item i{width:28px;height:28px;border-radius:50%;background:#c8c8ce;border:2px solid #9b9ba2;display:block;overflow:hidden}
.mission-card{position:absolute;height:78px;background:var(--card)}
.mission-card .avatar{position:absolute;left:12px;top:10px;width:58px;height:58px;border-radius:50%;background:var(--avatar);border:3px solid #a0a0a7;overflow:hidden}
.mission-card .who{position:absolute;left:84px;top:20px;font-size:14px;line-height:17px;color:#222;white-space:nowrap}
.mission-card .dot{position:absolute;top:32px;width:13px;height:13px;border-radius:50%;background:var(--blue)}
.mission-card .stats{position:absolute;top:4px;font-size:10px;line-height:24px;color:#333;white-space:nowrap}
.mission-card .mini{position:absolute;top:10px;width:64px;height:58px;background:#ececef;display:flex;align-items:center;justify-content:center}
.mission-card .add{position:absolute;top:26px;width:24px;height:24px;border-radius:50%;background:var(--green);color:#fff;font:700 20px/24px Arial,sans-serif;text-align:center}
.swipe{font-size:15px;color:#333;white-space:nowrap}
.swipe .dots{color:#aaa;letter-spacing:3px;margin-right:40px}
.activity-card{position:absolute;height:126px;background:var(--card);padding:12px 16px}
.activity-card .head{display:flex;align-items:center;gap:10px;font-size:15px;font-weight:500;color:#1f3f7a}
.activity-card .head i{width:13px;height:13px;border-radius:50%;background:var(--blue);display:block}
.activity-card .time{margin-left:auto;font-size:12px;color:#777;font-weight:400}
.activity-card .kind{font-size:15px;font-weight:700;color:#1f2a40;margin:4px 0 0 23px}
.activity-card .note{font-size:12px;color:#777;margin:4px 0 0 23px}

/* Team gallery */
.thumb{position:absolute;width:78px;height:80px}
.slider-dot{position:absolute;width:16px;height:16px;border-radius:50%;border:2px solid #8d8d94}
.slider-dot.current{background:#a8a8ae;border-color:#a8a8ae}

/* Footer */
.site-footer{position:absolute;left:0;top:2910px;width:1200px;height:90px;background:var(--footer);display:flex;justify-content:center;align-items:center;gap:34px;color:#fff;font-size:20px}
</style>
</head>
<body>
<div class="canvas">

  <header class="site-header">
    <div class="menu-toggle"><span></span><span></span><span></span></div>
    <div class="nav-missions">SEE THE MISSIONS</div>
    <div class="brand">HARBORWINGS</div>
    <div class="auth"><span>LOG IN</span><span>SIGN UP</span></div>
  </header>

  <section class="hero" role="img" aria-label="Black-and-white photograph of two smiling girls, the younger one eating fruit">
    <div class="hero-quote">
      <div class="verse">" She has a Name. He has dreams.<br>She hopes she would have a future.<br>He is like you."</div>
      <div class="pledge">" <b>1 USD</b> a month will help her and him".</div>
    </div>
  </section>
  <div class="hero-band"></div>

  <!-- About -->
  <section class="section section-about">
    <h2 class="section-title" style="top:10px">ABOUT</h2>

    <div class="abs mission-title" style="left:197px;top:70px">Mission: Orphan Maria, 11y</div>
    <div class="abs tabs" style="left:197px;top:108px;width:523px">
      <div class="active">Story</div><div>Updates</div><div>Comments</div>
    </div>

    <div class="timeline-rail" style="left:166px;top:196px;height:428px"></div>
    <div class="timeline-dot" style="left:155px;top:180px"></div>
    <div class="timeline-dot current" style="left:155px;top:392px"></div>
    <div class="timeline-dot" style="left:155px;top:610px"></div>

    <div class="abs story" style="left:193px;top:166px;width:505px">
      <p>Lorem ipsum dolor sit amet, sapien etiam, nunc amet dolor ac odio mauris justo. Luctus arcu, urna praesent at id quisque ac. Arcu es massa vestibulum malesuada, integer vivamus elit eu mauris eus, cum eros quis aliquam wisi. Nulla wisi laoreet suspendisse integer vivamus elit eu mauris hendrerit facilisi, mi mattis pariatur aliquam pharetra eget.</p>
      <p>Lorem ipsum dolor sit amet, sapien etiam, nunc amet dolor ac odio mauris justo. Luctus arcu, urna praesent at id quisque ac. Arcu es massa vestibulum malesuada, integer vivamus elit eu mauris eus, cum eros quis aliquam wisi. Nulla wisi laoreet suspendisse integer vivamus elit eu mauris hendrerit facilisi, mi mattis pariatur aliquam pharetra eget.</p>
    </div>
    <svg class="abs img-placeholder" style="left:193px;top:352px" width="502" height="110" role="img" aria-label="Story photo">
      <line x1="0" y1="0" x2="502" y2="110" stroke="#444" stroke-width="1.5"/><line x1="502" y1="0" x2="0" y2="110" stroke="#444" stroke-width="1.5"/>
    </svg>
    <div class="abs story" style="left:193px;top:476px;width:505px">
      <p>Lorem ipsum dolor sit amet, sapien etiam, nunc amet dolor ac odio mauris justo. Luctus arcu, urna praesent at id quisque ac. Arcu es massa vestibulum malesuada, integer vivamus elit eu mauris eus, cum eros quis aliquam wisi. Nulla wisi laoreet suspendisse integer vivamus elit eu mauris hendrerit facilisi, mi mattis pariatur aliquam pharetra eget.</p>
      <p>Lorem ipsum dolor sit amet, sapien etiam, nunc amet dolor ac odio mauris justo. Luctus arcu, urna praesent at id quisque ac. Arcu es massa vestibulum malesuada, integer vivamus elit eu mauris eus, cum eros quis aliquam wisi. Nulla wisi laoreet suspendisse integer vivamus elit eu mauris hendrerit facilisi, mi mattis pariatur aliquam pharetra eget.</p>
    </div>

    <!-- support panel -->
    <div class="abs kid-name" style="left:758px;top:70px">Name: Maria, 11y</div>
    <div class="abs meta" style="left:762px;top:118px">
      <svg width="14" height="18" viewBox="0 0 14 18"><path d="M7 0a7 7 0 0 0-7 7c0 5 7 11 7 11s7-6 7-11a7 7 0 0 0-7-7zm0 10a3 3 0 1 1 0-6 3 3 0 0 1 0 6z" fill="#777"/></svg>Kalkutta</div>
    <div class="abs meta" style="left:762px;top:146px">Organization: Jacob</div>
    <div class="abs support-row" style="left:758px;top:204px;width:296px">Support
      <div class="angels">
        <i class="angel"><svg viewBox="0 0 60 60"><circle cx="30" cy="23" r="11" fill="#8f8f96"/><path d="M8 60c2-14 11-21 22-21s20 7 22 21z" fill="#8f8f96"/></svg></i>
        <i class="angel"><svg viewBox="0 0 60 60"><circle cx="30" cy="23" r="11" fill="#8f8f96"/><path d="M8 60c2-14 11-21 22-21s20 7 22 21z" fill="#8f8f96"/></svg></i>
        <i class="angel"><svg viewBox="0 0 60 60"><circle cx="30" cy="23" r="11" fill="#8f8f96"/><path d="M8 60c2-14 11-21 22-21s20 7 22 21z" fill="#8f8f96"/></svg></i>
        <i class="angel"><svg viewBox="0 0 60 60"><circle cx="30" cy="23" r="11" fill="#8f8f96"/><path d="M8 60c2-14 11-21 22-21s20 7 22 21z" fill="#8f8f96"/></svg></i>
        <i class="angel"><svg viewBox="0 0 60 60"><circle cx="30" cy="23" r="11" fill="#8f8f96"/><path d="M8 60c2-14 11-21 22-21s20 7 22 21z" fill="#8f8f96"/></svg></i>
        <svg width="10" height="16"><path d="M2 2l6 6-6 6" stroke="#666" stroke-width="2" fill="none"/></svg></div>
    </div>
    <div class="abs my-support" style="left:756px;top:250px">My support is now: $5 / month <span class="close-dot">×</span></div>
    <div class="abs progress" style="left:758px;top:274px">
      <div class="progress-box">
        <svg width="92" height="92" viewBox="0 0 100 100"><circle cx="50" cy="50" r="38" fill="#e6e6ea" stroke="#a8a8ae" stroke-width="11"/><circle cx="50" cy="50" r="38" fill="none" stroke="#27a394" stroke-width="11" stroke-dasharray="107.5 238.8" transform="rotate(-90 50 50)"/><text x="50" y="57" text-anchor="middle" font-size="20" fill="#888" font-family="Roboto,sans-serif">45%</text></svg>
      </div>
      <div class="progress-text"><strong>$15 given</strong><br>of total $35 needed<br>
        <svg width="18" height="14" style="vertical-align:middle;margin-right:6px"><rect x="1" y="1" width="16" height="12" fill="none" stroke="#888"/><line x1="1" y1="5" x2="17" y2="5" stroke="#888"/></svg><span style="font-size:13px">per month need</span></div>
    </div>
    <div class="abs participate-label" style="left:750px;top:396px;width:304px">Participate</div>

    <div class="option" style="left:750px;top:432px;width:304px"><i class="check"></i>I am in, $1 / month<svg class="cart" width="26" height="20"><path d="M1 2h4l3 11h14l3-8H7" stroke="#aaa" stroke-width="1.5" fill="none"/><circle cx="10" cy="17" r="2" fill="#aaa"/><circle cx="20" cy="17" r="2" fill="#aaa"/></svg></div>
    <div class="option" style="left:750px;top:480px;width:304px"><i class="check"></i>Increased, $5 / month<svg class="cart" width="26" height="20"><path d="M1 2h4l3 11h14l3-8H7" stroke="#aaa" stroke-width="1.5" fill="none"/><circle cx="10" cy="17" r="2" fill="#aaa"/><circle cx="20" cy="17" r="2" fill="#aaa"/></svg></div>
    <div class="option" style="left:750px;top:527px;width:304px"><i class="check"></i>Decent help, $10 / month<svg class="cart" width="26" height="20"><path d="M1 2h4l3 11h14l3-8H7" stroke="#aaa" stroke-width="1.5" fill="none"/><circle cx="10" cy="17" r="2" fill="#aaa"/><circle cx="20" cy="17" r="2" fill="#aaa"/></svg></div>
    <div class="option" style="left:750px;top:574px;width:304px"><i class="check"></i>Whole kid, $35 / month<svg class="cart" width="26" height="20"><path d="M1 2h4l3 11h14l3-8H7" stroke="#aaa" stroke-width="1.5" fill="none"/><circle cx="10" cy="17" r="2" fill="#aaa"/><circle cx="20" cy="17" r="2" fill="#aaa"/></svg></div>
    <div class="option" style="left:750px;top:622px;width:304px"><i class="check"></i>My amount<span class="amount-input">Enter amount</span><svg class="cart" width="26" height="20"><path d="M1 2h4l3 11h14l3-8H7" stroke="#aaa" stroke-width="1.5" fill="none"/><circle cx="10" cy="17" r="2" fill="#aaa"/><circle cx="20" cy="17" r="2" fill="#aaa"/></svg></div>
  </section>

  <!-- Activities -->
  <section class="section section-activities">
    <h2 class="section-title" style="top:18px">ACTIVITIES</h2>

    <div class="profile-avatar" style="left:182px;top:72px"><svg viewBox="0 0 60 60"><circle cx="30" cy="23" r="11" fill="#8f8f96"/><path d="M8 60c2-14 11-21 22-21s20 7 22 21z" fill="#8f8f96"/></svg></div>
    <div class="abs profile-field" style="left:373px;top:104px">Name: MATTHEW MATT</div>
    <div class="abs profile-field" style="left:373px;top:138px">Username: matt28</div>

    <div class="abs label-caps" style="left:750px;top:104px">FOLLOWING</div>
    <div class="abs" style="left:750px;top:128px">
      <div class="follow-item"><i><svg viewBox="0 0 60 60"><circle cx="30" cy="23" r="11" fill="#8f8f96"/><path d="M8 60c2-14 11-21 22-21s20 7 22 21z" fill="#8f8f96"/></svg></i>Maria,...</div>
      <div class="follow-item"><i><svg viewBox="0 0 60 60"><circle cx="30" cy="23" r="11" fill="#8f8f96"/><path d="M8 60c2-14 11-21 22-21s20 7 22 21z" fill="#8f8f96"/></svg></i>Maria,...</div>
      <div class="follow-item"><i><svg viewBox="0 0 60 60"><circle cx="30" cy="23" r="11" fill="#8f8f96"/><path d="M8 60c2-14 11-21 22-21s20 7 22 21z" fill="#8f8f96"/></svg></i>Maria,...</div>
    </div>

    <div class="abs label-caps" style="left:176px;top:220px">MY MISSIONS
      <svg width="16" height="10" style="margin-left:8px"><path d="M2 2l6 6 6-6" stroke="#888" stroke-width="1.5" fill="none"/></svg></div>

    <div class="mission-card" style="left:176px;top:252px;width:416px">
      <i class="avatar"><svg viewBox="0 0 60 60"><circle cx="30" cy="23" r="11" fill="#8f8f96"/><path d="M8 60c2-14 11-21 22-21s20 7 22 21z" fill="#8f8f96"/></svg></i><div class="who">Maria, 11y<br>Orphan, Jacob</div><i class="dot" style="left:206px"></i>
      <div class="stats" style="left:248px">$15 raised<br>$20 to go<br>5 angels in</div>
      <div class="mini" style="left:305px"><svg width="54" height="54" viewBox="0 0 100 100"><circle cx="50" cy="50" r="38" fill="#fff" stroke="#c4c4c9" stroke-width="10"/><circle cx="50" cy="50" r="38" fill="none" stroke="#27a394" stroke-width="10" stroke-dasharray="107.5 238.8" transform="rotate(-90 50 50)"/><text x="50" y="57" text-anchor="middle" font-size="20" fill="#999" font-family="Roboto,sans-serif">45%</text></svg></div>
      <i class="add" style="left:380px">+</i>
    </div>
    <div class="mission-card" style="left:176px;top:334px;width:416px">
      <i class="avatar"><svg viewBox="0 0 60 60"><circle cx="30" cy="23" r="11" fill="#8f8f96"/><path d="M8 60c2-14 11-21 22-21s20 7 22 21z" fill="#8f8f96"/></svg></i><div class="who">Matthew, 11y<br>Orphan, Jacob</div><i class="dot" style="left:206px"></i>
      <div class="stats" style="left:248px">$15 raised<br>$20 to go<br>5 angels in</div>
      <div class="mini" style="left:305px"><svg width="54" height="54" viewBox="0 0 100 100"><circle cx="50" cy="50" r="38" fill="#fff" stroke="#c4c4c9" stroke-width="10"/><circle cx="50" cy="50" r="38" fill="none" stroke="#27a394" stroke-width="10" stroke-dasharray="107.5 238.8" transform="rotate(-90 50 50)"/><text x="50" y="57" text-anchor="middle" font-size="20" fill="#999" font-family="Roboto,sans-serif">45%</text></svg></div>
      <i class="add" style="left:380px">+</i>
    </div>
    <div class="mission-card" style="left:176px;top:414px;width:416px">
      <i class="avatar"><svg viewBox="0 0 60 60"><circle cx="30" cy="23" r="11" fill="#8f8f96"/><path d="M8 60c2-14 11-21 22-21s20 7 22 21z" fill="#8f8f96"/></svg></i><div class="who">Maria, 11y<br>Orphan, Jacob</div><i class="dot" style="left:206px"></i>
      <div class="stats" style="left:248px">$15 raised<br>$20 to go<br>5 angels in</div>
      <div class="mini" style="left:305px"><svg width="54" height="54" viewBox="0 0 100 100"><circle cx="50" cy="50" r="38" fill="#fff" stroke="#c4c4c9" stroke-width="10"/><circle cx="50" cy="50" r="38" fill="none" stroke="#27a394" stroke-width="10" stroke-dasharray="107.5 238.8" transform="rotate(-90 50 50)"/><text x="50" y="57" text-anchor="middle" font-size="20" fill="#999" font-family="Roboto,sans-serif">45%</text></svg></div>
      <i class="add" style="left:380px">+</i>
    </div>

    <div class="mission-card" style="left:618px;top:252px;width:418px">
      <i class="avatar"><svg viewBox="0 0 60 60"><circle cx="30" cy="23" r="11" fill="#8f8f96"/><path d="M8 60c2-14 11-21 22-21s20 7 22 21z" fill="#8f8f96"/></svg></i><div class="who">Maria, 11y<br>Orphan, Jacob</div>
      <div class="mini" style="left:305px"><svg width="54" height="54" viewBox="0 0 100 100"><circle cx="50" cy="50" r="38" fill="#fff" stroke="#c4c4c9" stroke-width="10"/><circle cx="50" cy="50" r="38" fill="none" stroke="#27a394" stroke-width="10" stroke-dasharray="107.5 238.8" transform="rotate(-90 50 50)"/><text x="50" y="57" text-anchor="middle" font-size="20" fill="#999" font-family="Roboto,sans-serif">45%</text></svg></div>
      <i class="add" style="left:382px">+</i>
    </div>
    <div class="mission-card" style="left:618px;top:334px;width:418px">
      <i class="avatar"><svg viewBox="0 0 60 60"><circle cx="30" cy="23" r="11" fill="#8f8f96"/><path d="M8 60c2-14 11-21 22-21s20 7 22 21z" fill="#8f8f96"/></svg></i><div class="who">Matthew, 11y<br>Orphan, Jacob</div>
      <div class="stats" style="left:248px">$15 raised<br>$20 to go<br>5 angels in</div>
      <div class="mini" style="left:305px"><svg width="54" height="54" viewBox="0 0 100 100"><circle cx="50" cy="50" r="38" fill="#fff" stroke="#c4c4c9" stroke-width="10"/><circle cx="50" cy="50" r="38" fill="none" stroke="#27a394" stroke-width="10" stroke-dasharray="107.5 238.8" transform="rotate(-90 50 50)"/><text x="50" y="57" text-anchor="middle" font-size="20" fill="#999" font-family="Roboto,sans-serif">45%</text></svg></div>
      <i class="add" style="left:382px">+</i>
    </div>
    <div class="abs swipe" style="left:811px;top:452px"><span class="dots">···</span>Swipe to <span style="margin-left:24px">see more?</span></div>

    <div class="abs label-caps" style="left:176px;top:500px">ACTIVITIES
      <svg width="10" height="16" style="margin-left:10px;vertical-align:middle"><path d="M2 2l6 6-6 6" stroke="#888" stroke-width="1.5" fill="none"/></svg></div>

    <div class="activity-card" style="left:176px;top:532px;width:394px">
      <div class="head"><i></i>Maria<span class="time">10:51 AM</span></div>
      <div class="kind">Report</div>
      <div class="note">Half year report.....</div>
    </div>
    <div class="activity-card" style="left:582px;top:532px;width:397px">
      <div class="head"><i></i>Maria<span class="time">10:51 AM</span></div>
      <div class="kind">Got a new angel</div>
      <div class="note" style="margin-left:160px;margin-top:14px">Anonymous</div>
    </div>
    <div class="activity-card" style="left:176px;top:668px;width:394px">
      <div class="head"><i></i>Imma Mustard<span class="time">10:51 AM</span></div>
    </div>
    <div class="activity-card" style="left:582px;top:668px;width:397px">
      <div class="head"><i></i>Matthew<span class="time">10:51 AM</span></div>
    </div>
  </section>

  <!-- Team -->
  <section class="section section-team">
    <h2 class="section-title" style="top:8px">TEAM</h2>

    <svg class="abs img-placeholder" style="left:195px;top:66px" width="518" height="230" role="img" aria-label="Team photo">
      <line x1="0" y1="0" x2="518" y2="230" stroke="#444" stroke-width="1.5"/><line x1="518" y1="0" x2="0" y2="230" stroke="#444" stroke-width="1.5"/>
    </svg>
    <svg class="abs" style="left:196px;top:334px" width="14" height="30"><path d="M11 2L3 15l8 13" stroke="#555" stroke-width="2" fill="none"/></svg>
    <svg class="abs" style="left:696px;top:334px" width="14" height="30"><path d="M3 2l8 13-8 13" stroke="#555" stroke-width="2" fill="none"/></svg>
    <svg class="thumb img-placeholder" style="left:237px;top:308px" viewBox="0 0 78 80" role="img" aria-label="Gallery thumbnail"><line x1="0" y1="0" x2="78" y2="80" stroke="#444"/><line x1="78" y1="0" x2="0" y2="80" stroke="#444"/></svg>
    <svg class="thumb img-placeholder" style="left:328px;top:308px" viewBox="0 0 78 80" role="img" aria-label="Gallery thumbnail"><line x1="0" y1="0" x2="78" y2="80" stroke="#444"/><line x1="78" y1="0" x2="0" y2="80" stroke="#444"/></svg>
    <svg class="thumb img-placeholder" style="left:419px;top:308px" viewBox="0 0 78 80" role="img" aria-label="Gallery thumbnail"><line x1="0" y1="0" x2="78" y2="80" stroke="#444"/><line x1="78" y1="0" x2="0" y2="80" stroke="#444"/></svg>
    <svg class="thumb img-placeholder" style="left:510px;top:308px" viewBox="0 0 78 80" role="img" aria-label="Gallery thumbnail"><line x1="0" y1="0" x2="78" y2="80" stroke="#444"/><line x1="78" y1="0" x2="0" y2="80" stroke="#444"/></svg>
    <svg class="thumb img-placeholder" style="left:601px;top:308px" viewBox="0 0 78 80" role="img" aria-label="Gallery thumbnail"><line x1="0" y1="0" x2="78" y2="80" stroke="#444"/><line x1="78" y1="0" x2="0" y2="80" stroke="#444"/></svg>

    <div class="abs mission-title" style="left:211px;top:404px">Mission: Orphan Maria, 11y</div>
    <div class="abs tabs" style="left:211px;top:450px;width:511px">
      <div class="active">Story</div><div>Updates</div><div>Comments</div>
    </div>
    <div class="slider-dot current" style="left:170px;top:524px"></div>
    <div class="slider-dot" style="left:170px;top:553px"></div>
    <div class="slider-dot" style="left:170px;top:581px"></div>
    <div class="abs story" style="left:211px;top:490px;width:505px">
      <p>Lorem ipsum dolor sit amet, sapien etiam, nunc amet dolor ac odio mauris justo. Luctus arcu, urna praesent at id quisque ac. Arcu es massa vestibulum malesuada, integer vivamus elit eu mauris eus, cum eros quis aliquam wisi. Nulla wisi laoreet suspendisse integer vivamus elit eu mauris hendrerit facilisi, mi mattis pariatur aliquam pharetra eget.</p>
      <p>Lorem ipsum dolor sit amet, sapien etiam, nunc amet dolor ac odio mauris justo. Luctus arcu, urna praesent at id quisque ac. Arcu es massa vestibulum malesuada, integer vivamus elit eu mauris eus, cum eros quis aliquam wisi. Nulla wisi laoreet suspendisse integer vivamus elit</p>
    </div>

    <div class="abs kid-name" style="left:750px;top:76px">Name: Maria, 11y</div>
    <div class="abs meta" style="left:754px;top:122px">
      <svg width="14" height="18" viewBox="0 0 14 18"><path d="M7 0a7 7 0 0 0-7 7c0 5 7 11 7 11s7-6 7-11a7 7 0 0 0-7-7zm0 10a3 3 0 1 1 0-6 3 3 0 0 1 0 6z" fill="#777"/></svg>Kalkutta</div>
    <div class="abs meta" style="left:754px;top:150px">Organization: Jacob</div>
    <div class="abs support-row" style="left:750px;top:180px;width:290px">Support
      <div class="angels">
        <i class="angel"><svg viewBox="0 0 60 60"><circle cx="30" cy="23" r="11" fill="#8f8f96"/><path d="M8 60c2-14 11-21 22-21s20 7 22 21z" fill="#8f8f96"/></svg></i>
        <i class="angel"><svg viewBox="0 0 60 60"><circle cx="30" cy="23" r="11" fill="#8f8f96"/><path d="M8 60c2-14 11-21 22-21s20 7 22 21z" fill="#8f8f96"/></svg></i>
        <i class="angel"><svg viewBox="0 0 60 60"><circle cx="30" cy="23" r="11" fill="#8f8f96"/><path d="M8 60c2-14 11-21 22-21s20 7 22 21z" fill="#8f8f96"/></svg></i>
        <i class="angel"><svg viewBox="0 0 60 60"><circle cx="30" cy="23" r="11" fill="#8f8f96"/><path d="M8 60c2-14 11-21 22-21s20 7 22 21z" fill="#8f8f96"/></svg></i>
        <i class="angel"><svg viewBox="0 0 60 60"><circle cx="30" cy="23" r="11" fill="#8f8f96"/><path d="M8 60c2-14 11-21 22-21s20 7 22 21z" fill="#8f8f96"/></svg></i>
        <svg width="10" height="16"><path d="M2 2l6 6-6 6" stroke="#666" stroke-width="2" fill="none"/></svg></div>
    </div>
    <div class="abs my-support" style="left:744px;top:226px">My support is now: $5 / month <span class="close-dot">×</span></div>
    <div class="abs progress" style="left:750px;top:252px">
      <div class="progress-box">
        <svg width="92" height="92" viewBox="0 0 100 100"><circle cx="50" cy="50" r="38" fill="#e6e6ea" stroke="#a8a8ae" stroke-width="11"/><circle cx="50" cy="50" r="38" fill="none" stroke="#27a394" stroke-width="11" stroke-dasharray="107.5 238.8" transform="rotate(-90 50 50)"/><text x="50" y="57" text-anchor="middle" font-size="20" fill="#888" font-family="Roboto,sans-serif">45%</text></svg>
      </div>
      <div class="progress-text"><strong>$15 given</strong><br>of total $35 needed<br>
        <svg width="18" height="14" style="vertical-align:middle;margin-right:6px"><rect x="1" y="1" width="16" height="12" fill="none" stroke="#888"/><line x1="1" y1="5" x2="17" y2="5" stroke="#888"/></svg><span style="font-size:13px">per month need</span></div>
    </div>
    <div class="abs participate-label" style="left:744px;top:386px;width:296px">Participate</div>

    <div class="option" style="left:744px;top:428px;width:294px"><i class="check"></i>I am in, $1</div>
    <div class="option" style="left:744px;top:476px;width:294px"><i class="check"></i>Increased, $5 / month</div>
    <div class="option" style="left:744px;top:523px;width:294px"><i class="check"></i>Decent help, $10 / month</div>
    <div class="option" style="left:744px;top:568px;width:294px"><i class="check"></i>Whole kid, $35 / month</div>
    <div class="option" style="left:744px;top:616px;width:294px"><i class="check"></i>My amount<span class="amount-input" style="margin-left:30px">Enter amount</span></div>
  </section>

  <footer class="site-footer">
    <span>Contact</span><span>Download</span><span>Press</span><span>Email</span><span>Support</span><span>Privacy Policy</span>
  </footer>
</div>
</body>
</html>
```